Email Notification & Marketing Templates

I want to start with something like a newsletter or informational email, but i need Top Tips to Detect Phishing Scams. Something that i can send to users so they can follow it when receiving or exchanging emails. I will also need promotional items for my company that i can send to customers as well. It can be based on on our website QRVLINK.COM

Will also need:
newsletters
announcements
marketing emails
alerts
security notifications

Examples:Items such as Security Awareness Poster Series
Phishing Awareness
Password Security
Email Attachments
QR Code scams
Public WiFi safety

```html
<!DOCTYPE html>
<html lang="en">
<head>
<meta charset="utf-8">
<title>Think Before You Click Attachments</title>
<link href="https://fonts.googleapis.com/css2?family=Montserrat:wght@500;600;700;800;900&display=swap" rel="stylesheet">
<style>
  :root{
    --page:#ffffff;
    --brand-green:#2f8a12;
    --headline-dark:#14520a;
    --headline-light:#2e8c14;
    --panel:#1d3a27;
    --panel-edge:#142a1c;
    --alert-yellow:#f6c619;
    --alert-ink:#1e3312;
    --accent-green:#84c73d;
    --body-ink:#f2f5f0;
    --button:#3d8a1d;
    --button-edge:#6cbf3a;
    --threat-red:#e2261b;
    --screen-dark:#1a1c1e;
  }
  *{margin:0;padding:0;box-sizing:border-box}
  html,body{width:800px;height:1200px;overflow:hidden;background:var(--page)}
  body{position:relative;font-family:"Montserrat",sans-serif}

  .brand{position:absolute;top:26px;left:0;width:800px;display:flex;justify-content:center;align-items:center;gap:14px}
  .brand-mark{width:34px;height:34px;background:var(--brand-green)}
  .brand-name{font-weight:800;font-size:44px;color:var(--brand-green);letter-spacing:-1px;font-family:"Montserrat",sans-serif}

  .headline{position:absolute;top:140px;left:0;width:800px;text-align:center;font-weight:900;font-size:55px;line-height:57px;letter-spacing:-2px;
    background:linear-gradient(180deg,var(--headline-light),var(--headline-dark));-webkit-background-clip:text;background-clip:text;color:transparent}

  .hero{position:absolute;left:74px;top:283px;width:649px;height:401px;border-radius:10px;
    background:radial-gradient(ellipse at 50% 58%,#c0241a 0%,#5a1410 26%,var(--screen-dark) 60%),var(--screen-dark);
    box-shadow:0 0 40px 14px rgba(40,40,40,.35)}
  .hero-bar{position:absolute;left:0;top:30px;width:100%;height:44px;background:linear-gradient(90deg,#6fb23a,#9bd34a)}
  .hero-top{position:absolute;left:0;top:0;width:100%;height:30px;background:#2a2c2e;border-radius:10px 10px 0 0}

  .panel{position:absolute;left:14px;top:734px;width:771px;height:430px;border-radius:12px;
    background:radial-gradient(ellipse at 40% 30%,#254a31,var(--panel) 60%,var(--panel-edge))}

  .alert-banner{position:absolute;left:51px;top:709px;width:697px;height:53px;background:var(--alert-yellow);border-radius:4px;
    display:flex;align-items:center;gap:12px;padding-left:28px;color:var(--alert-ink);font-weight:700;font-size:24px;letter-spacing:-.6px}
  .alert-banner svg{width:42px;height:38px}

  .intro{position:absolute;left:56px;top:782px;width:690px;color:var(--body-ink);font-size:18px;font-weight:500;line-height:27px}

  .rules{position:absolute;left:58px;top:850px;width:700px;list-style:none}
  .rule{position:relative;padding-left:28px;color:var(--body-ink);font-size:17.5px;font-weight:500;line-height:25px;margin-bottom:13px}
  .rule svg{position:absolute;left:0;top:5px;width:21px;height:17px}
  .rule-title{color:var(--accent-green);font-weight:700;font-size:21.5px;letter-spacing:-.4px}
  .rule strong{font-weight:700;color:#fff}

  .report-button{position:absolute;left:221px;top:1086px;width:359px;height:45px;border-radius:5px;
    background:linear-gradient(180deg,#4fa027,var(--button) 60%,#2b6a14);border:1.5px solid var(--button-edge);
    color:#fff;font-weight:700;font-size:20px;letter-spacing:-.3px;display:flex;align-items:center;justify-content:center}
</style>
</head>
<body>
  <header class="brand">
    <span class="brand-mark"></span>
    <span class="brand-name">Qorvane Link Networks</span>
  </header>

  <h1 class="headline">THINK BEFORE YOU!<br>CLICK ATTACHMENTS</h1>

  <div class="hero" role="img" aria-label="Illustration of an email window titled Important Document Attached, showing a glowing red attachment with a skull and crossbones flanked by warning triangles">
    <div class="hero-top"></div>
    <div class="hero-bar"></div>
  </div>

  <section class="panel"></section>

  <div class="alert-banner">
    <svg viewBox="0 0 42 38"><path d="M21 3 L39 35 H3 Z" fill="none" stroke="#1e3312" stroke-width="3" stroke-linejoin="round"/><rect x="19.5" y="13" width="3" height="12" fill="#1e3312"/><rect x="19.5" y="28" width="3" height="3" fill="#1e3312"/></svg>
    Beware of Suspicious Email Attachments!
  </div>

  <p class="intro">Cybercriminals often use email attachments to deliver malware.<br>Be cautious and protect yourself by following these key rules:</p>

  <ul class="rules">
    <li class="rule"><svg viewBox="0 0 21 17"><path d="M2 9 L8 15 L19 2" fill="none" stroke="#84c73d" stroke-width="3.5" stroke-linecap="round" stroke-linejoin="round"/></svg><span class="rule-title">Strangers:</span> Don’t open attachments from <strong>unknown</strong> senders.</li>
    <li class="rule"><svg viewBox="0 0 21 17"><path d="M2 9 L8 15 L19 2" fill="none" stroke="#84c73d" stroke-width="3.5" stroke-linecap="round" stroke-linejoin="round"/></svg><span class="rule-title">Surprise Files:</span> Be wary of <strong>unexpected</strong> attachments, even from known contacts.</li>
    <li class="rule"><svg viewBox="0 0 21 17"><path d="M2 9 L8 15 L19 2" fill="none" stroke="#84c73d" stroke-width="3.5" stroke-linecap="round" stroke-linejoin="round"/></svg><span class="rule-title">Suspicious File Types:</span> Avoid opening files like <strong>.zip</strong>, <strong>exe</strong>, or <strong>.scr</strong> from emails.</li>
    <li class="rule"><svg viewBox="0 0 21 17"><path d="M2 9 L8 15 L19 2" fill="none" stroke="#84c73d" stroke-width="3.5" stroke-linecap="round" stroke-linejoin="round"/></svg><span class="rule-title">Check Before Click:</span> Carefully review the sender’s email address and the email content.</li>
  </ul>

  <div class="report-button">REPORT SUSPICIOUS EMAIL</div>
</body>
</html>
```